Landing Page für Freelancer im Bereich der Informationstechnik
Zielgruppe
Ich bin Experte für Informationstechnik, Unified Communications, Beratung, Management sowie Projekte aller Art.
Mit meiner WOLKENTOR GmbH bin ich als (einzelner) Freelancer für mittelständische Unternehmen und Konzerne in verschiedensten Projekten tätig.
Mein Motto lautet 'Mit Präzision und langjähriger Erfahrung immer alles im Griff!'
Aufgabenstellung
Die aktuell existierende Internet-Präsenz unter wolkentor-web.de beinhaltet aktuell nur eine minimalistische statische Seite sowie das Impressum, ohne jegliche dynamische Inhalte.
DABEI SOLL ES BLEIBEN. Auch die Inhalte sollen unverändert übernommen werden.
Lediglich soll jetzt eine Anlehnung an das zwischenzeitlich vorhandene Logo vorgenommen werden, welches ich mitliefere.
Es geht mir insgesamt nur darum, ein professionelleres Auftreten zu haben, WENN sich denn mal jemand auf die Seite verirrt.
Das Aussehen soll daher modern und dynamisch sein.
ZUSAMMENFASSUNG: Inhalte bleiben 1:1, grafische Anpassung an Logo gewünscht.
Technisch: Statisch, kein Content-Management. Lohnt sich hier nicht.
SEHR WICHTIG: Ich möchte gerne, dass die Lieferung bereits als HTML (und NICHT NUR ALS GRAFIK) erfolgt, ggf. stelle ich auch kurz den FTP-Zugang.
Insgesamt möchte ich gar keine große Sache draus machen.
Viele Anpassungsrunden wird es voraussichtlich nicht geben.
Zeitlich ist dies hier ein sehr kleines Projekt - Erweiterungen kommen später.

```html
<!DOCTYPE html>
<html lang="de">
<head>
<meta charset="utf-8">
<title>WOLKENTOR GmbH – Lukas Peter Brandt</title>
<link rel="stylesheet" href="https://fonts.googleapis.com/css2?family=Outfit:wght@400;500;600&display=swap">
<style>
  :root {
    --ink: #3f4145;
    --accent: #52a9c2;
    --rule: #9fd0dc;
    --hero-start: #ece6ef;
    --hero-mid: #cfd2e8;
    --hero-end: #a5b3db;
    --panel: rgba(255, 255, 255, 0.86);
    --page: #ffffff;
  }
  * { margin: 0; padding: 0; box-sizing: border-box; }
  html, body {
    width: 1097px;
    height: 1200px;
    overflow: hidden;
    background: var(--page);
    font-family: "Outfit", sans-serif;
    color: var(--ink);
  }
  .page { position: relative; width: 1097px; height: 1200px; }

  .hero {
    position: absolute; left: 0; top: 0;
    width: 1097px; height: 503px;
    background: linear-gradient(120deg, var(--hero-start) 0%, var(--hero-mid) 50%, var(--hero-end) 100%);
  }
  .hero-panel {
    position: absolute; left: 106px; top: 70px;
    width: 433px; height: 433px;
    background: var(--panel);
  }
  .brand-name {
    position: absolute; left: 0; top: 150px; width: 100%;
    text-align: center;
    font-size: 21px; font-weight: 500; letter-spacing: 3px;
    color: var(--ink);
  }
  .motto {
    position: absolute; left: 0; top: 286px; width: 100%;
    text-align: center;
    font-size: 18px; font-weight: 500; line-height: 28.5px;
    text-transform: uppercase;
    color: var(--ink);
  }

  .title-pre {
    position: absolute; left: 106px; top: 602px;
    font-size: 21px; font-weight: 500;
  }
  .person-name {
    position: absolute; left: 104px; top: 648px;
    font-size: 42px; font-weight: 500; color: var(--accent);
  }
  .title-post {
    position: absolute; left: 106px; top: 718px;
    font-size: 21px; font-weight: 500;
  }

  .contact-mail {
    position: absolute; left: 106px; top: 827px;
    font-size: 12.5px; font-weight: 500; color: var(--ink);
    text-decoration: none;
    border-bottom: 1px solid var(--accent);
    padding-bottom: 2px;
  }

  .expertise {
    position: absolute; left: 446px; top: 820px; width: 560px;
    font-size: 31px; font-weight: 500; line-height: 41.5px;
  }
  .intro {
    position: absolute; left: 446px; top: 972px; width: 540px;
    font-size: 12.3px; font-weight: 500; line-height: 19px;
  }

  .footer-rule {
    position: absolute; left: 106px; top: 1092px;
    width: 885px; height: 1px; background: var(--rule);
  }
  .footer-nav { position: absolute; left: 106px; top: 1140px; display: flex; gap: 38px; }
  .footer-nav a {
    font-size: 12.5px; font-weight: 500; color: var(--ink); text-decoration: none;
  }
</style>
</head>
<body>
<div class="page">
  <header class="hero" role="img" aria-label="Illustration eines Schreibtischs von oben mit Monitor, Laptop, Tastatur, Smartphone und Kaffeetasse">
    <div class="hero-panel">
      <div class="brand-name">WOLKENTOR GmbH</div>
      <p class="motto">"Mit Präzision und<br>langjähriger Erfahrung immer<br>alles im Griff!"</p>
    </div>
  </header>

  <main>
    <p class="title-pre">Diplom-Informatiker (FH)</p>
    <h1 class="person-name">Lukas Peter Brandt</h1>
    <p class="title-post">Master of Science in Electronic Business</p>

    <a class="contact-mail" href="#">l punkt brandt at wolkentor punkt de</a>

    <h2 class="expertise">Experte für Informationstechnik | Unified Communications | Beratung | Management | Projekte aller Art</h2>
    <p class="intro">Gerne schicke ich Ihnen unverbindlich mein Expertenprofil samt CV sowie meine aktuellen Verfügbarkeiten zu. Kontaktieren Sie mich hierzu einfach per E-Mail unter l punkt brandt at wolkentor punkt de. Ich freue mich auf Sie!</p>
  </main>

  <div class="footer-rule"></div>
  <nav class="footer-nav">
    <a href="#">Startseite</a>
    <a href="#">Impressum</a>
    <a href="#">Datenschutz</a>
  </nav>
</div>
</body>
</html>
```